Business Card Design Project

double sided, embossed, name & logo on front font sonsie one, back Name Marisol Venkamp, mobile 0468201934, Phone 73519086,
email marisol@brightspanservices.com, use sysbols on the back for example an envelope for email, a telephone for phone number etc.symbol slate grey writing navy blue

Industry/Entity Type

Business

```html
<!DOCTYPE html>
<html lang="en">
<head>
<meta charset="utf-8">
<title>Brightspan Services – Business Card</title>
<link rel="stylesheet" href="https://fonts.googleapis.com/css2?family=Sonsie+One&family=Lobster+Two:ital,wght@1,700&display=swap">
<style>
  :root {
    --page: #ffffff;
    --card-white: #ffffff;
    --card-tint: #c9fbff;
    --navy: #1b2a6b;
    --slate: #708090;
    --shadow: rgba(0, 0, 0, 0.55);
  }
  * { margin: 0; padding: 0; box-sizing: border-box; }
  html, body {
    width: 1040px;
    height: 1200px;
    overflow: hidden;
    background: var(--page);
  }
  .canvas {
    position: relative;
    width: 1040px;
    height: 1200px;
  }
  .card {
    position: absolute;
    left: 22px;
    width: 972px;
    border-radius: 20px;
    box-shadow: 6px 8px 12px var(--shadow);
    overflow: hidden;
  }
  .card--front {
    top: 22px;
    height: 540px;
    background: linear-gradient(150deg, var(--card-tint) 0%, var(--card-white) 35%, var(--card-white) 60%, var(--card-tint) 100%);
  }
  .card--back {
    top: 604px;
    height: 546px;
    background: linear-gradient(150deg, var(--card-tint) 0%, var(--card-white) 40%, var(--card-white) 65%, var(--card-tint) 100%);
  }
  .brand {
    position: absolute;
    left: 0;
    right: 0;
    top: 262px;
    display: flex;
    justify-content: center;
    align-items: center;
    gap: 22px;
  }
  .brand-name {
    font-family: "Sonsie One", cursive;
    font-size: 50px;
    line-height: 1.2;
    color: var(--navy);
    white-space: nowrap;
  }
  .brand-mark {
    width: 78px;
    height: 78px;
    flex: none;
    border-radius: 50%;
    background: var(--slate);
  }
  .holder-name {
    position: absolute;
    left: 0;
    right: 0;
    top: 212px;
    text-align: center;
    font-family: "Sonsie One", cursive;
    font-size: 54px;
    font-weight: 400;
    line-height: 1.2;
    color: var(--navy);
    white-space: nowrap;
  }
  .contacts {
    position: absolute;
    left: 0;
    right: 0;
    top: 420px;
    display: flex;
    flex-direction: column;
    align-items: center;
    gap: 8px;
    font-family: "Lobster Two", cursive;
    font-style: italic;
    font-weight: 700;
    font-size: 44px;
    line-height: 1.1;
    letter-spacing: 2.5px;
    color: var(--navy);
  }
  .contact-row {
    display: flex;
    align-items: center;
    gap: 60px;
  }
  .contact-item {
    display: flex;
    align-items: center;
    gap: 14px;
    white-space: nowrap;
  }
  .contact-icon {
    width: 32px;
    height: 32px;
    flex: none;
    fill: var(--slate);
  }
</style>
</head>
<body>
<main class="canvas">
  <section class="card card--front" aria-label="Card front">
    <div class="brand">
      <p class="brand-name">Brightspan Services</p>
      <span class="brand-mark" aria-hidden="true"></span>
    </div>
  </section>

  <section class="card card--back" aria-label="Card back">
    <h1 class="holder-name">Marisol Venkamp</h1>
    <div class="contacts">
      <div class="contact-row">
        <span class="contact-item">
          <svg class="contact-icon" viewBox="0 0 30 30" aria-label="Mobile">
            <rect x="7" y="2" width="16" height="26" rx="4"/>
            <rect x="10" y="6" width="10" height="15" rx="1" fill="#ffffff"/>
            <circle cx="15" cy="24.5" r="1.6" fill="#ffffff"/>
          </svg>
          0468201934
        </span>
        <span class="contact-item">
          <svg class="contact-icon" viewBox="0 0 30 30" aria-label="Phone">
            <circle cx="15" cy="15" r="14"/>
            <path d="M10 8c1-1 2.3-.8 3 .4l1.2 2.2c.5 1 .2 2-.7 2.6l-.9.6c.8 2 2.5 3.7 4.5 4.5l.6-.9c.6-.9 1.6-1.2 2.6-.7l2.2 1.2c1.2.7 1.4 2 .4 3-1.6 1.6-3.8 2-6 .9-3.4-1.6-6-4.2-7.6-7.6-1.1-2.2-.7-4.4.7-6.2z" fill="#ffffff"/>
          </svg>
          73519086
        </span>
      </div>
      <div class="contact-row">
        <span class="contact-item">
          <svg class="contact-icon" viewBox="0 0 30 30" aria-label="Email">
            <rect x="2" y="6" width="26" height="18" rx="2"/>
            <path d="M4 8.5l11 8 11-8M4 22l8-7M26 22l-8-7" fill="none" stroke="#ffffff" stroke-width="1.8"/>
          </svg>
          marisol@brightspanservices.com
        </span>
      </div>
    </div>
  </section>
</main>
</body>
</html>
```